Modern Label for Loose Tea pouches on 4.5x6 Label

We need a new label for our teas that is very simple in design, but stylish and modern. This will be used to print labels for our loose tea pouches. The label will be at max 4.5x6 inches in size. There should be a place for the tea name, description, ingredients, and size that is changeable.
Preferably an AI file that allows me to setup variables to change the above items. There will also need to be our logo which is supplied, and our address on the label.
Address:
Brindle Teas
148 Lower Ferncliff Lane
Alderbrook, VT 05031
Target Market(s)
Tea Lovers
Requirements
Must have
- Adobe Illustrator file with variables setup for replacement of tea name, description, ingredients, and size (weights 2oz, 4oz, 8oz, 1lb)

```html
<!DOCTYPE html>
<html lang="en">
<head>
<meta charset="utf-8">
<title>Brindle Teas – Green Tea Tropical Label</title>
<link rel="stylesheet" href="https://fonts.googleapis.com/css2?family=Pathway+Gothic+One&family=Tinos:ital@1&family=Arimo&family=Cousine&display=swap">
<style>
  :root {
    --backdrop: #2b2b2b;
    --lime: #bcd631;
    --pink: #dd4f9c;
    --paper: #ffffff;
    --ink: #2a2a2a;
    --ink-soft: #3a3a3a;
  }
  * { margin: 0; padding: 0; box-sizing: border-box; }
  html, body {
    width: 956px; height: 1200px; overflow: hidden;
    background: var(--backdrop);
  }
  .label {
    position: relative;
    width: 956px; height: 1200px;
    background: var(--backdrop);
  }
  .label__bands {
    position: absolute; left: 0; top: 0;
  }
  .sender-address {
    position: absolute; left: 68px; top: 118px;
    font-family: "Cousine", monospace;
    font-style: normal;
    font-size: 27px; line-height: 43px;
    letter-spacing: 1px;
    color: var(--ink);
  }
  .pack-size {
    position: absolute; left: 706px; top: 166px;
    font-family: "Arimo", sans-serif;
    font-size: 33px;
    color: var(--ink);
  }
  .brand-name {
    position: absolute; left: 47px; width: 782px; top: 512px;
    display: flex; align-items: center; justify-content: center; gap: 24px;
    font-family: "Pathway Gothic One", sans-serif;
    font-size: 106px; line-height: 1;
    letter-spacing: 6px;
    color: var(--pink);
  }
  .brand-name__dot {
    width: 36px; height: 36px; border-radius: 50%;
    background: var(--lime);
  }
  .tea-name {
    position: absolute; left: 75px; width: 782px; top: 658px;
    text-align: center;
    font-family: "Pathway Gothic One", sans-serif;
    font-weight: 400;
    font-size: 100px; line-height: 1;
    color: var(--ink-soft);
  }
  .field-label {
    position: absolute; left: 47px; width: 782px;
    text-align: center;
    font-family: "Tinos", serif; font-style: italic;
    font-size: 31px;
    letter-spacing: 41px;
    padding-left: 41px;
    color: var(--ink);
  }
  .field-label--ingredients { top: 848px; }
  .field-label--description { top: 966px; }
</style>
</head>
<body>
  <div class="label">
    <svg class="label__bands" width="956" height="1200" viewBox="0 0 956 1200" aria-hidden="true">
      <rect class="band-lime" x="47" y="0" width="862" height="605" fill="var(--lime)"/>
      <rect class="band-pink" x="47" y="605" width="862" height="575" fill="var(--pink)"/>
      <polygon class="paper-panel" points="47,113 829,113 829,1083 47,1096" fill="var(--paper)"/>
    </svg>

    <address class="sender-address">
      Brindle Teas<br>
      148 Lower Ferncliff Lane<br>
      Alderbrook, VT 05031
    </address>

    <div class="pack-size">100g</div>

    <div class="brand-name"><span class="brand-name__dot"></span>BRINDLE TEAS</div>

    <h1 class="tea-name">GREEN TEA TROPICAL</h1>

    <p class="field-label field-label--ingredients">Ingredients</p>
    <p class="field-label field-label--description">Description</p>
  </div>
</body>
</html>
```